Simple Banners for several sites

I'm looking for banners in the following formats for the sites listed bellow:

* Leaderboard
* Wide Skyscraper
* Skyscaper
* Square Button
* Micro bar
* Full banner
* Half Banner
* Medium Rectangle

The websites:
* http://notavault.crenmop.com/
* http://quolet.com/
* http://dravimunto.com/

I would like to get 1 sets of banners for each website, and I'ld like you to submit each set/site independently.

```html
<!DOCTYPE html>
<html lang="en">
<head>
<meta charset="UTF-8">
<title>Quolet banner set</title>
<link rel="stylesheet" href="https://fonts.googleapis.com/css2?family=Open+Sans:wght@600&family=Arimo:wght@400;700&display=swap">
<style>
  :root {
    --stage: #e8e2da;
    --panel: #f1f1ef;
    --ink: #4a4a48;
    --rule: #55524e;
    --red-top: #e8252b;
    --red-bottom: #a10b10;
    --button-edge: #7a0a0d;
    --white: #ffffff;
    --black: #111111;
    --device-light: #dcdde0;
    --device-dark: #3a3c40;
  }
  * { box-sizing: border-box; margin: 0; padding: 0; }
  html, body { width: 1200px; height: 900px; overflow: hidden; }
  body {
    position: relative;
    background: var(--stage);
    font-family: "Arimo", Arial, sans-serif;
    color: var(--ink);
  }
  .banner {
    position: absolute;
    background: var(--panel);
    box-shadow: 0 2px 8px rgba(0,0,0,0.18);
    overflow: hidden;
  }
  .brand {
    position: absolute;
    font-family: "Open Sans", Arial, sans-serif;
    font-weight: 600;
    color: var(--ink);
    letter-spacing: 1px;
    line-height: 1;
    text-align: center;
    white-space: nowrap;
  }
  .divider { position: absolute; background: var(--rule); }
  .tagline {
    position: absolute;
    text-align: center;
    color: var(--ink);
    white-space: nowrap;
  }
  .tagline strong { font-weight: 700; }
  .tagline span { display: block; }
  .device-art {
    position: absolute;
    background: linear-gradient(135deg, var(--device-dark) 0%, var(--device-dark) 22%, var(--device-light) 45%, #c9d3e0 70%, var(--panel) 100%);
    border-radius: 4px;
  }
  .cta {
    position: absolute;
    border-radius: 20px;
    background: linear-gradient(var(--red-top), var(--red-bottom));
    border: 1px solid var(--button-edge);
    box-shadow: inset 0 1px 0 rgba(255,255,255,0.35), 0 1px 2px rgba(0,0,0,0.3);
    color: var(--white);
    font-weight: 700;
    text-align: center;
    text-shadow: 0 0 2px var(--black), 0 1px 1px var(--black);
    letter-spacing: -0.5px;
    white-space: nowrap;
  }
  .site-url {
    position: absolute;
    font-weight: 700;
    color: var(--black);
    text-align: center;
  }

  /* Leaderboard */
  .leaderboard { left: 214px; top: 49px; width: 853px; height: 105px; }
  .leaderboard .brand { left: 19px; top: 33px; width: 180px; font-size: 40px; text-align: left; }
  .leaderboard .divider { left: 215px; top: 0; width: 4px; height: 105px; }
  .leaderboard .tagline { left: 250px; top: 3px; width: 260px; font-size: 30px; line-height: 32px; }
  .leaderboard .device-art { left: 555px; top: 4px; width: 108px; height: 100px; }
  .leaderboard .cta { left: 689px; top: 30px; width: 146px; height: 39px; font-size: 23px; line-height: 37px; }
  .leaderboard .site-url { left: 689px; top: 73px; width: 146px; font-size: 13px; }

  /* Square */
  .square { left: 341px; top: 302px; width: 351px; height: 292px; }
  .square .brand { left: 0; top: 10px; width: 351px; font-size: 50px; }
  .square .divider { left: 0; top: 62px; width: 351px; height: 4px; }
  .square .device-art { left: 4px; top: 73px; width: 116px; height: 196px; }
  .square .tagline { left: 122px; top: 94px; width: 226px; font-size: 26px; line-height: 31px; }
  .square .cta { left: 198px; top: 211px; width: 146px; height: 37px; font-size: 22px; line-height: 35px; }
  .square .site-url { left: 198px; top: 253px; width: 146px; font-size: 13px; }

  /* Skyscraper */
  .skyscraper { left: 809px; top: 179px; width: 187px; height: 702px; }
  .skyscraper .brand { left: 0; top: 42px; width: 187px; font-size: 44px; }
  .skyscraper .divider { left: 0; top: 119px; width: 187px; height: 4px; }
  .skyscraper .tagline { left: 0; top: 163px; width: 187px; font-size: 29px; line-height: 37px; }
  .skyscraper .device-art { left: 8px; top: 328px; width: 176px; height: 198px; }
  .skyscraper .cta { left: 20px; top: 611px; width: 146px; height: 39px; font-size: 23px; line-height: 37px; }
  .skyscraper .site-url { left: 0; top: 655px; width: 187px; font-size: 13px; }
</style>
</head>
<body>

<section class="banner leaderboard" aria-label="Leaderboard banner">
  <div class="brand">QUOLET</div>
  <div class="divider"></div>
  <p class="tagline">
    <span>Your <strong>MAGAZINE</strong></span>
    <span>for Everything</span>
    <span><strong>DIGITAL</strong></span>
  </p>
  <div class="device-art" role="img" aria-label="Tablet with stacked magazine pages"></div>
  <div class="cta">CLICK HERE</div>
  <div class="site-url">www.quolet.com</div>
</section>

<section class="banner square" aria-label="Medium rectangle banner">
  <div class="brand">QUOLET</div>
  <div class="divider"></div>
  <div class="device-art" role="img" aria-label="Tablet with stacked magazine pages"></div>
  <p class="tagline">
    <span>Your <strong>MAGAZINE</strong></span>
    <span>for Everything</span>
    <span><strong>DIGITAL</strong></span>
  </p>
  <div class="cta">CLICK HERE</div>
  <div class="site-url">www.quolet.com</div>
</section>

<section class="banner skyscraper" aria-label="Skyscraper banner">
  <div class="brand">QUOLET</div>
  <div class="divider"></div>
  <p class="tagline">
    <span>Your</span>
    <span><strong>MAGAZINE</strong></span>
    <span>for Everything</span>
    <span><strong>DIGITAL</strong></span>
  </p>
  <div class="device-art" role="img" aria-label="Tablet with stacked magazine pages"></div>
  <div class="cta">CLICK HERE</div>
  <div class="site-url">www.quolet.com</div>
</section>

</body>
</html>
```